Need Flyer Design for real estate

Need a generic Flyer Design for real estate Company..

See few flyers attached for an ideas..need to have 4 directors pictures n contact details in one side (back side)..

Industry/Entity Type

Real Estate

Requirements
Must have
• Our Logo Colours..
• PANTONE 484 C ( RED)
• PANTONE 2766 C ( BLUE)

```html
<!DOCTYPE html>
<html lang="en">
<head>
<meta charset="utf-8">
<title>Meridian Real Estate – Selling or Buying Flyer</title>
<link href="https://fonts.googleapis.com/css2?family=Kaushan+Script&family=Lato:ital,wght@0,400;0,700;1,700&display=swap" rel="stylesheet">
<style>
  :root {
    --brand-red: #8e1f30;
    --brand-navy: #1c2260;
    --ink: #111111;
    --paper: #ffffff;
    --photo-light: #e9e4dc;
    --photo-wood: #9a7a5c;
    --photo-sky: #cfdbe3;
  }
  html, body {
    margin: 0;
    padding: 0;
    overflow: hidden;
    background: var(--paper);
  }
  .flyer {
    position: relative;
    width: 1200px;
    height: 567px;
    overflow: hidden;
    background: var(--paper);
    font-family: "Lato", Arial, sans-serif;
    color: var(--ink);
  }
  .flyer__shapes {
    position: absolute;
    inset: 0;
    z-index: 0;
  }
  .brand-box {
    position: absolute;
    z-index: 1;
    left: 0;
    top: 0;
    width: 372px;
    height: 206px;
    background: var(--brand-navy);
    display: flex;
    align-items: center;
    justify-content: center;
    gap: 14px;
  }
  .brand-box__dot {
    width: 14px;
    height: 14px;
    background: var(--paper);
  }
  .brand-box__name {
    color: var(--paper);
    font-size: 28px;
    font-weight: 400;
    letter-spacing: 3px;
    text-transform: uppercase;
    line-height: 1.25;
  }
  .headline {
    position: absolute;
    z-index: 1;
    left: 428px;
    top: 12px;
    margin: 0;
    font-family: "Kaushan Script", cursive;
    font-weight: 400;
    font-size: 58px;
    line-height: 74px;
    color: var(--brand-navy);
    white-space: nowrap;
  }
  .headline__lead { color: var(--brand-red); display: block; }
  .headline__line { display: block; }
  .pitch {
    position: absolute;
    z-index: 1;
    left: 14px;
    top: 262px;
    margin: 0;
    font-size: 23px;
    line-height: 34px;
    white-space: nowrap;
  }
  .tagline {
    position: absolute;
    z-index: 1;
    left: 14px;
    top: 366px;
    margin: 0;
    font-size: 24px;
    font-weight: 700;
    font-style: italic;
    color: var(--brand-navy);
    white-space: nowrap;
  }
  .contact {
    position: absolute;
    z-index: 1;
    left: 26px;
    top: 448px;
    color: var(--paper);
  }
  .contact__label {
    font-size: 32px;
    font-weight: 700;
    line-height: 40px;
  }
  .contact__phone {
    font-size: 44px;
    font-weight: 400;
    line-height: 54px;
  }
</style>
</head>
<body>
<main class="flyer">
  <svg class="flyer__shapes" width="1200" height="567" viewBox="0 0 1200 567">
    <defs>
      <linearGradient id="interiorTones" x1="0" y1="0" x2="1" y2="1">
        <stop offset="0" stop-color="#9a7a5c"/>
        <stop offset="0.35" stop-color="#cfdbe3"/>
        <stop offset="0.7" stop-color="#e9e4dc"/>
        <stop offset="1" stop-color="#9a7a5c"/>
      </linearGradient>
      <linearGradient id="coupleTones" x1="0" y1="0" x2="0" y2="1">
        <stop offset="0" stop-color="#6b4a36"/>
        <stop offset="0.4" stop-color="#d9b39a"/>
        <stop offset="1" stop-color="#a9b7d4"/>
      </linearGradient>
    </defs>

    <path class="sweep sweep--red" fill="#8e1f30"
          d="M760 0 H800 C800 300 730 500 660 567 H0 V415 C560 410 760 300 760 0 Z"/>
    <path class="sweep sweep--navy" fill="#1c2260"
          d="M790 0 H820 C820 300 760 480 690 567 H650 C730 470 790 300 790 0 Z"/>
    <path class="band-divider" fill="none" stroke="#ffffff" stroke-width="3"
          d="M0 436 C220 430 440 455 560 567"/>

    <path class="photo photo--interior" role="img"
          aria-label="Photograph of a bright modern living room with timber ceiling, large windows and lounge seating"
          fill="url(#interiorTones)"
          d="M832 0 H1200 V567 H705 C785 470 832 300 832 0 Z"/>

    <path class="photo photo--couple" role="img"
          aria-label="Photograph of a smiling couple giving a thumbs up"
          fill="url(#coupleTones)"
          d="M565 567 C565 440 605 392 690 392 C770 392 810 440 815 567 Z"/>
  </svg>

  <div class="brand-box">
    <span class="brand-box__dot"></span>
    <span class="brand-box__name">Meridian<br>Real Estate</span>
  </div>

  <h1 class="headline">
    <span class="headline__lead">Thinking of</span>
    <span class="headline__line">Selling or</span>
    <span class="headline__line">Buying?</span>
  </h1>

  <p class="pitch">Our team is most capable with best negotiating skills<br>and with total commitment to achieving the best<br>results for you.</p>
  <p class="tagline">You can relax while we do all the work..!</p>

  <div class="contact">
    <div class="contact__label">Call Us:</div>
    <div class="contact__phone">000 000 0000</div>
  </div>
</main>
</body>
</html>
```